Bref créative
PRDL
Stationary & Business Cards
I need double sided standard sized Business Card [3.5" x 2"]
non specific
Modern
Pine Ridge Dragster League
www.prdlmotors-example.com
info@prdlmotors-example.com
The Pine Ridge Dragster League showcases the best of heads up and index drag racing for racers, fans and families!
Visit the PRDL website for more information & race dates.

```html
<!DOCTYPE html>
<html lang="en">
<head>
<meta charset="utf-8">
<title>PRDL Stationery &amp; Business Cards</title>
<link rel="stylesheet" href="https://fonts.googleapis.com/css2?family=Roboto:wght@400;700;900&display=swap">
<style>
:root{
  --bg:#e7e4df;
  --paper:#ffffff;
  --red:#d3212c;
  --red-dark:#a3121b;
  --black:#1a1a1a;
  --charcoal:#2b2b2b;
  --grey:#8a8a8a;
  --rule:#bdbdbd;
  --label:#ffffff;
  --label-bg:#3a3a3a;
}
*{box-sizing:border-box;margin:0;padding:0}
html,body{width:1200px;height:832px;overflow:hidden}
body{background:var(--bg);font-family:"Roboto",Arial,sans-serif;color:var(--black);position:relative}
.piece{position:absolute;background:var(--paper);box-shadow:0 2px 6px rgba(0,0,0,.25);overflow:hidden}
.option-label{position:absolute;font-weight:700;font-size:17px;color:var(--label-bg)}
.brand{display:flex;align-items:center;justify-content:center;gap:6px;font-weight:900;color:var(--black);letter-spacing:1px}
.brand .dot{width:.7em;height:.7em;border-radius:50%;background:var(--red)}
.brand.on-dark{color:#fff}
.footer-url{position:absolute;bottom:10px;left:0;right:0;text-align:center;font-size:6px;color:var(--grey)}

/* Letterhead 1 – fax */
.fax{left:34px;top:43px;width:300px;height:413px}
.fax .brand{position:absolute;top:20px;left:0;right:0;font-size:16px}
.fax .fax-title{position:absolute;top:88px;left:20px;font-size:26px;font-weight:400}
.fax .fields{position:absolute;top:132px;left:20px;right:20px;display:grid;grid-template-columns:1fr 1fr;column-gap:16px;row-gap:12px}
.fax .field{font-size:7px;color:var(--grey);border-bottom:1px solid var(--rule);padding-bottom:2px}
.fax .checks{position:absolute;top:235px;left:20px;right:10px;display:flex;gap:11px;font-size:6.5px;color:var(--grey)}
.fax .checks span::before{content:"";display:inline-block;width:6px;height:6px;border:1px solid var(--grey);margin-right:3px;vertical-align:-1px}

/* Letterhead 2 */
.letter-two{left:372px;top:43px;width:312px;height:413px}
.letter-two .band{position:absolute;top:6px;left:0;right:0;height:22px;background:var(--red);border-bottom:5px solid var(--black)}
.letter-two .brand{position:absolute;top:40px;left:0;right:0;font-size:14px}
.letter-two .url-top{position:absolute;top:60px;left:0;right:0;text-align:center;font-size:5px;color:var(--grey)}

/* Letterhead 3 */
.letter-three{left:710px;top:43px;width:315px;height:413px}
.letter-three .brand{position:absolute;top:20px;left:0;right:0;font-size:18px}
.letter-three .band{position:absolute;bottom:16px;left:0;right:0;height:7px;background:var(--red)}
.letter-three .footer-url{bottom:5px}

/* Envelopes */
.envelope-one{left:38px;top:475px;width:315px;height:199px}
.envelope-one .flap{position:absolute;top:0;left:0;right:0;height:40px;background:var(--charcoal)}
.envelope-one .flap .dot{position:absolute;left:50%;top:14px;width:26px;height:12px;margin-left:-13px;border-radius:50%;background:var(--red)}
.envelope-one .brand{position:absolute;top:58px;left:18px;font-size:16px}
.envelope-one .lines{position:absolute;bottom:28px;left:0;right:0;height:8px;border-top:4px solid var(--red);border-bottom:1px solid var(--red)}

.envelope-two{left:413px;top:475px;width:312px;height:199px}
.envelope-two .flap{position:absolute;top:0;left:0;right:0;height:40px;background:var(--red)}
.envelope-two .brand{position:absolute;top:58px;left:18px;font-size:16px}
.envelope-two .stripes{position:absolute;bottom:18px;left:0;right:0;height:22px;background:var(--black);border-top:6px solid var(--red);border-bottom:4px solid #fff;box-shadow:0 4px 0 var(--black)}

/* Business cards */
.card{width:182px}
.card.dark{background:linear-gradient(180deg,#2f2f2f,#0f0f0f)}
.card .band{position:absolute;left:0;right:0;height:14px;background:var(--red);border-top:1px solid var(--red-dark);border-bottom:1px solid var(--red-dark)}
.card .brand{position:absolute;left:0;right:0}
.card .blurb{position:absolute;top:12px;left:14px;right:14px;text-align:center;font-size:5.2px;line-height:1.45;color:#555}
.card.dark .blurb{color:#ddd}
.card .card-url{position:absolute;left:0;right:0;text-align:center;font-size:5px;color:var(--grey)}

.card-a{left:802px;top:475px;height:91px}
.card-b{left:802px;top:576px;height:103px}
.card-c{left:802px;top:691px;height:108px}
.card-d{left:994px;top:475px;height:91px}
.card-e{left:994px;top:576px;height:103px}
.card-f{left:994px;top:691px;height:108px}
</style>
</head>
<body>

<div class="option-label" style="left:163px;top:12px">Option 1</div>
<div class="option-label" style="left:497px;top:12px">Option 2</div>
<div class="option-label" style="left:818px;top:12px">Option 3</div>

<section class="piece fax">
  <div class="brand"><span class="dot"></span>PRDL</div>
  <div class="fax-title">FAX</div>
  <div class="fields">
    <div class="field">To:</div><div class="field">From:</div>
    <div class="field">Fax:</div><div class="field">Pages:</div>
    <div class="field">Phone:</div><div class="field">Date:</div>
    <div class="field">Re:</div><div class="field">CC:</div>
  </div>
  <div class="checks"><span>Urgent</span><span>For Review</span><span>Please Comment</span><span>Please Reply</span><span>Please Recycle</span></div>
  <div class="footer-url">www.prdlmotors-example.com</div>
</section>

<section class="piece letter-two">
  <div class="band"></div>
  <div class="brand"><span class="dot"></span>PRDL</div>
  <div class="url-top">www.prdlmotors-example.com</div>
</section>

<section class="piece letter-three">
  <div class="brand"><span class="dot"></span>PRDL</div>
  <div class="band"></div>
  <div class="footer-url">www.prdlmotors-example.com</div>
</section>

<section class="piece envelope-one">
  <div class="flap"><span class="dot"></span></div>
  <div class="brand"><span class="dot"></span>PRDL</div>
  <div class="lines"></div>
</section>
<div class="option-label" style="left:163px;top:684px">Option 1</div>

<section class="piece envelope-two">
  <div class="flap"></div>
  <div class="brand"><span class="dot"></span>PRDL</div>
  <div class="stripes"></div>
</section>
<div class="option-label" style="left:538px;top:684px">Option 2</div>

<section class="piece card dark card-a">
  <div class="band" style="top:38px"></div>
  <div class="brand on-dark" style="top:34px;font-size:17px"><span class="dot"></span>PRDL</div>
  <div class="card-url" style="bottom:8px">www.prdlmotors-example.com</div>
</section>

<section class="piece card dark card-b">
  <p class="blurb">The Pine Ridge Dragster League showcases the best of heads up and index drag racing for racers, fans and families! Visit the PRDL website for more information &amp; race dates.</p>
  <div class="band" style="top:66px"></div>
  <div class="brand on-dark" style="top:63px;font-size:13px"><span class="dot"></span>PRDL</div>
  <div class="card-url" style="bottom:6px">www.prdlmotors-example.com</div>
</section>

<section class="piece card dark card-c">
  <p class="blurb">The Pine Ridge Dragster League showcases the best of heads up and index drag racing for racers, fans and families! Visit the PRDL website for more information &amp; race dates.</p>
  <div class="band" style="top:70px"></div>
  <div class="brand on-dark" style="top:67px;font-size:13px"><span class="dot"></span>PRDL</div>
  <div class="card-url" style="bottom:6px">info@prdlmotors-example.com</div>
</section>

<section class="piece card card-d">
  <div class="band" style="top:38px"></div>
  <div class="brand" style="top:20px;font-size:17px"><span class="dot"></span>PRDL</div>
  <div class="card-url" style="bottom:8px">www.prdlmotors-example.com</div>
</section>

<section class="piece card card-e">
  <p class="blurb">The Pine Ridge Dragster League showcases the best of heads up and index drag racing for racers, fans and families! Visit the PRDL website for more information &amp; race dates.</p>
  <div class="band" style="top:66px"></div>
  <div class="brand on-dark" style="top:63px;font-size:13px"><span class="dot" style="background:#fff"></span>PRDL</div>
  <div class="card-url" style="bottom:6px">www.prdlmotors-example.com</div>
</section>

<section class="piece card card-f">
  <p class="blurb">The Pine Ridge Dragster League showcases the best of heads up and index drag racing for racers, fans and families! Visit the PRDL website for more information &amp; race dates.</p>
  <div class="band" style="top:70px"></div>
  <div class="brand on-dark" style="top:67px;font-size:13px"><span class="dot" style="background:#fff"></span>PRDL</div>
  <div class="card-url" style="bottom:6px">info@prdlmotors-example.com</div>
</section>

</body>
</html>
```